Business Card Design

We service, sell & install vehicle hoists in automotive workshops & would like the colours royal blue or green incorporated into the design.

Industry/Entity Type

Automotive

Contact Information for Business Card

KTL Lifts
Equipment Sales & Service
Colin Marwick 0412 781 359
Dean Corbett 0417 925 163
14 Lyall Street Kyneton Vic 3444
email: ktllifts@mailbox.example.au

```html
<!DOCTYPE html>
<html lang="en">
<head>
<meta charset="utf-8">
<title>KTL Lifts Equipment – Business Card</title>
<link rel="stylesheet" href="https://fonts.googleapis.com/css2?family=Barlow:wght@300;400;600;700&display=swap">
<style>
  :root {
    --navy: #1f2a78;
    --grey-text: #4a4c55;
    --card: #f7f6f2;
    --backdrop: #e6e3de;
  }
  * { margin: 0; padding: 0; box-sizing: border-box; }
  html, body {
    width: 1200px;
    height: 918px;
    overflow: hidden;
    background: var(--backdrop);
    font-family: "Barlow", Arial, sans-serif;
  }
  .card {
    position: absolute;
    left: 150px;
    top: 184px;
    width: 900px;
    height: 550px;
    background: var(--card);
    overflow: hidden;
  }
  .brand {
    position: absolute;
    left: 70px;
    top: 48px;
  }
  .brand__name {
    font-size: 46px;
    font-weight: 700;
    color: var(--navy);
    line-height: 1.1;
    letter-spacing: 0.2px;
  }
  .brand__tagline {
    font-size: 32px;
    font-weight: 300;
    color: var(--grey-text);
    line-height: 1.2;
  }
  .brand-mark {
    position: absolute;
    left: 70px;
    top: 228px;
    width: 130px;
    height: 130px;
    border-radius: 50%;
    background: var(--navy);
  }
  .contacts {
    position: absolute;
    left: 495px;
    top: 268px;
    font-size: 26px;
    line-height: 40px;
  }
  .contact { display: flex; gap: 20px; }
  .contact__name { font-weight: 700; color: var(--navy); width: 185px; }
  .contact__phone { font-weight: 400; color: var(--grey-text); }
  .details {
    position: absolute;
    left: 495px;
    top: 385px;
    font-size: 24px;
    line-height: 36px;
  }
  .details__address { font-weight: 700; color: var(--navy); }
  .details__email { font-weight: 400; color: var(--grey-text); }
</style>
</head>
<body>
  <main class="card">
    <header class="brand">
      <h1 class="brand__name">KTL Lifts Equipment</h1>
      <p class="brand__tagline">Sales &amp; Service</p>
    </header>

    <div class="brand-mark" aria-hidden="true"></div>

    <section class="contacts">
      <p class="contact"><span class="contact__name">Colin Marwick</span><span class="contact__phone">0412 781 359</span></p>
      <p class="contact"><span class="contact__name">Dean Corbett</span><span class="contact__phone">0417 925 163</span></p>
    </section>

    <section class="details">
      <p class="details__address">14 Lyall Street Kyneton Vic 3444</p>
      <p class="details__email">Email: ktllifts@mailbox.example.au</p>
    </section>
  </main>
</body>
</html>
```